Book Cover design: Waltz beside a Heron.

I need a front and back cover for my book called 'Waltz beside a Heron'.
It is self development book for help a person to be a better coach.
It is a metaphor. Dance is asking questions and the octopus is the person you are coaching (complex with my 'tentacles').
The audience would be adults. so want the cover to capture attention and also show that is have something of interest inside.
I have attach my first attempt. Please be bold.
The best sellers in this market place have simple but clear front page & back pages.

All the words are important but the sub-title is likely to change.

Target Market(s)

Adults who work with each other.
More business type people.

Industry/Entity Type

Leadership

Font styles to use
Serif

Requirements
Must have
• My project must have... The words that in the draft mock up.
• 'Waltz beside a Heron' [TITLE]
• 'A Map for Honest Mentoring'[SUB-TITLE]
• How to create inspiration and accountability using
• Five Critical Moments.[SUB_TITLE]
• By Godfrey T Haswell
Nice to have
• Clever and simple.

```html
<!DOCTYPE html>
<html lang="en">
<head>
<meta charset="utf-8">
<title>Waltz beside a Heron — Book Cover</title>
<link rel="stylesheet" href="https://fonts.googleapis.com/css2?family=Tinos:wght@400;700&family=Roboto+Condensed:wght@700&display=swap">
<style>
  :root {
    --paper: #ffffff;
    --sky: #afcfec;
    --sky-pale: #dde9f6;
    --ink: #545454;
    --label: #a88a80;
    --label-text: #ffffff;
    --rule: #c9c9c9;
  }
  html, body {
    margin: 0;
    padding: 0;
    overflow: hidden;
    background: var(--paper);
  }
  .canvas {
    position: relative;
    width: 1200px;
    height: 933px;
    overflow: hidden;
    background: var(--paper);
  }
  .cover-shapes {
    position: absolute;
    inset: 0;
  }
  .illustration {
    position: absolute;
    background: var(--sky-pale);
    border-radius: 50%;
    opacity: 0.7;
  }
  .illustration--back { left: 323px; top: 652px; width: 247px; height: 188px; }
  .illustration--front { left: 893px; top: 150px; width: 255px; height: 188px; }

  .series-label {
    position: absolute;
    left: 605px;
    top: 93px;
    height: 42px;
    padding: 0 8px;
    background: var(--label);
    color: var(--label-text);
    font-family: "Tinos", serif;
    font-size: 23px;
    line-height: 42px;
    white-space: nowrap;
  }
  .title {
    position: absolute;
    left: 640px;
    top: 188px;
    width: 470px;
    margin: 0;
    color: var(--ink);
    font-family: "Tinos", serif;
    font-weight: 700;
    text-align: center;
    text-transform: uppercase;
    line-height: 1;
  }
  .title__big {
    display: block;
    font-size: 86px;
    letter-spacing: 2px;
  }
  .title__small {
    display: block;
    font-size: 33px;
    letter-spacing: 1px;
    margin: 14px 0 18px;
  }
  .tagline {
    position: absolute;
    left: 622px;
    top: 594px;
    margin: 0;
    color: var(--ink);
    font-family: "Tinos", serif;
    font-weight: 700;
    font-size: 17px;
    line-height: 24px;
    letter-spacing: 1.2px;
    word-spacing: 4px;
    text-transform: uppercase;
  }
  .author {
    position: absolute;
    right: 82px;
    top: 784px;
    margin: 0;
    color: var(--ink);
    font-family: "Roboto Condensed", sans-serif;
    font-weight: 700;
    font-size: 31px;
    letter-spacing: 0.5px;
    text-transform: uppercase;
  }
</style>
</head>
<body>
<main class="canvas">
  <svg class="cover-shapes" width="1200" height="933" viewBox="0 0 1200 933" aria-hidden="true">
    <polygon class="back-band" points="57,86 600,86 600,615 57,383" fill="var(--sky)"/>
    <line class="back-rule" x1="57" y1="850" x2="600" y2="850" stroke="var(--rule)" stroke-width="1.5"/>
    <polygon class="front-band" points="606,375 1148,615 1148,850 606,850" fill="var(--sky)"/>
  </svg>

  <div class="illustration illustration--back" role="img" aria-label="Light blue line drawing of a smiling octopus with curling tentacles"></div>
  <div class="illustration illustration--front" role="img" aria-label="Light blue line drawing of a smiling octopus with curling tentacles"></div>

  <div class="series-label">'A Map for Honest Mentoring'</div>

  <h1 class="title">
    <span class="title__big">Waltz</span>
    <span class="title__small">beside a</span>
    <span class="title__big">Heron</span>
  </h1>

  <p class="tagline">How to create<br>inspiration and accountability<br>using five critical coaching moments</p>

  <p class="author">Godfrey T Haswell</p>
</main>
</body>
</html>
```